Basketball Coaching Presentation

Design and enhance a word document into a power point or google slides document. Document will be used in a interview setting to walk through my philosophy and concepts as the coach. i would like it to pop and have some basketballs, backboard, rim net, court type graphics added. My text my change, be edited or evolve over time. must be easy to edit in the future.
Make Cover page...i will insert my name later

```html
<!DOCTYPE html>
<html lang="en">
<head>
<meta charset="utf-8">
<title>Basketball Coaching Presentation</title>
<link rel="stylesheet" href="https://fonts.googleapis.com/css2?family=Montserrat:wght@500;600;700&family=Roboto+Condensed:wght@400;500&display=swap">
<style>
:root{
  --green:#7cc242;
  --navy:#1f1d5c;
  --board:#e4e4e4;
  --paper:#ffffff;
  --ink:#2a2a33;
  --rule:#b9dc98;
  --box-grey:#eef0ed;
  --box-green:#eef5e2;
}
*{margin:0;padding:0;box-sizing:border-box}
html,body{width:919px;height:1200px;overflow:hidden;background:var(--board)}
body{position:relative;font-family:"Roboto Condensed",Arial,sans-serif;color:var(--ink)}
.page{position:absolute;width:235px;height:333px;background:var(--paper);overflow:hidden;box-shadow:0 3px 10px rgba(0,0,0,.18)}
.abs{position:absolute}
.head{font-family:"Montserrat",Arial,sans-serif;font-weight:700;line-height:1.05}
.g{color:var(--green)} .n{color:var(--navy)} .w{color:#fff}
.photo{position:absolute}
.pnum{position:absolute;font-size:4.5px;font-family:"Montserrat",Arial,sans-serif;font-weight:600}
ul.list{list-style:none;position:absolute;font-size:5px;line-height:1.38}
ul.list li{position:relative;padding-left:6px;padding-bottom:2.6px;margin-bottom:2.6px;border-bottom:.5px solid var(--rule)}
ul.list li:last-child{border-bottom:none}
ul.list li::before{content:"";position:absolute;left:0;top:1.6px;width:3px;height:3px;background:var(--green)}
ul.list.plain li{border-bottom:none;padding-bottom:1px}
ul.list.navy-dot li::before{background:var(--navy)}

/* page 1 */
.cover{left:63px;top:79px}
.cover .band{left:0;top:0;width:235px;height:157px;background:var(--green)}
.cover .hero{left:27px;top:34px;width:179px;height:210px;background:radial-gradient(circle at 65% 42%,#e07a1c 0,#9a4a12 22%,#3a1e0c 55%,#140b06 100%)}
.cover .tagline{left:35px;top:197px;font-size:11px;font-weight:600;color:#fff;line-height:1.2}
.cover .name{left:28px;top:253px;font-size:7.5px;font-family:"Montserrat",Arial,sans-serif;font-weight:500;color:var(--ink)}
.cover .title{left:28px;top:266px;font-size:10.5px}
.cover .rule{left:27px;top:299px;width:182px;height:.6px;background:var(--green)}
.cover .contact{left:29px;top:306px;display:flex;align-items:center;gap:6px;font-size:4px;font-family:"Montserrat",Arial,sans-serif;font-weight:600;color:var(--navy)}
.cover .contact .tel{font-size:6px}
.cover .contact span{display:flex;align-items:center;gap:2px}
.cover .foot{left:0;top:319px;width:235px;height:14px;background:var(--navy)}

/* page 2 */
.mission{left:342px;top:79px}
.mission .heading{left:19px;top:21px;font-size:12px}
.mission .sq{display:inline-block;width:9px;height:9px;background:var(--green);margin-left:3px;vertical-align:-1px}
.mission .body{left:19px;top:54px;width:88px;font-size:5.1px;line-height:9px}
.mission .team{left:0;top:190px;width:103px;height:143px;background:var(--navy)}
.mission .team .head{position:absolute;left:0;top:44px;width:103px;text-align:center;font-size:12px;line-height:1.28}

/* page 3 */
.practice{left:621px;top:79px}
.practice .bar{left:0;top:14px;width:5px;height:45px;background:var(--green)}
.practice .heading{left:16px;top:20px;font-size:14px}
.practice .lower{left:0;top:213px;width:235px;height:120px;background:var(--navy)}
.practice .actions-title{left:0;top:255px;width:235px;text-align:center;font-size:11.5px}
.practice .actions{left:46px;top:274px;width:143px;text-align:center;font-size:5.3px;line-height:10px;color:#fff}

/* page 4 */
.offense{left:63px;top:436px}
.offense .top{left:0;top:0;width:235px;height:123px;background:var(--navy)}
.offense .col-head{top:29px;font-size:12.5px}
.offense .col-head .light{font-weight:500;display:block}
.offense .tick{top:26px;width:22px;height:.7px;background:#8b89b8}
.offense .box{top:66px;height:155px;padding:7px 5px}
.offense .box ul.list{position:static;font-size:4.9px}
.offense .box ul.list li{padding-left:0;border-bottom-color:#c9cdc5}
.offense .box ul.list li::before{display:none}
.offense .system{left:26px;top:246px;font-size:12px}

/* page 5 */
.numbers{left:342px;top:436px}
.numbers .tag{left:34px;width:57px;height:48px;display:flex;align-items:center;padding-left:7px;font-size:8px;font-family:"Montserrat",Arial,sans-serif;font-weight:600;color:#fff;line-height:1.2}
.numbers .val{left:98px;width:110px;font-size:5.1px;line-height:11px}
.numbers .line{left:92px;width:115px;height:.6px;background:var(--rule)}
.numbers .lower{left:0;top:191px;width:235px;height:142px;background:linear-gradient(115deg,#1f2a5c 0,#2a4f4a 45%,#4f8a3c 100%)}
.numbers .vr{left:15px;width:.8px;background:var(--green)}
.numbers .sub{left:22px;font-size:9.5px}
.numbers .txt{left:22px;width:135px;font-size:5px;line-height:8.3px;color:#fff}

/* page 6 */
.wellness{left:621px;top:436px}
.wellness .circle{position:absolute;border-radius:50%;text-align:center}
.wellness .c1{left:51px;top:27px;width:132px;height:132px;background:#fff;box-shadow:0 3px 8px rgba(0,0,0,.25)}
.wellness .c2{left:57px;top:114px;width:120px;height:120px;background:var(--green);box-shadow:0 3px 8px rgba(0,0,0,.25)}
.wellness .c3{left:73px;top:212px;width:88px;height:88px;background:radial-gradient(circle at 40% 45%,#c9a646 0,#2d6a5a 38%,#134a3f 100%);box-shadow:0 3px 8px rgba(0,0,0,.3)}

/* page 7 */
.parent{left:338px;top:800px}
.parent .rail{left:187px;top:0;width:48px;height:333px;background:var(--navy)}
.parent .label{left:9px;width:112px;height:21px;display:flex;align-items:center;padding-left:11px;font-size:9.5px;font-family:"Montserrat",Arial,sans-serif;font-weight:600}
</style>
</head>
<body>

<!-- Cover -->
<section class="page cover">
  <div class="abs band"></div>
  <div class="photo hero" role="img" aria-label="Basketball dropping through an orange rim and white net against a dark background"></div>
  <p class="abs tagline head" style="font-weight:600">Empowering<br>Athletes, Building<br>Champions</p>
  <p class="abs name">[Your Name]</p>
  <h1 class="abs title head"><span class="g">Basketball Coaching</span><br><span class="n">Presentation</span></h1>
  <div class="abs rule"></div>
  <div class="abs contact">
    <span class="tel"><svg width="6" height="6" viewBox="0 0 10 10"><path d="M2 1l2 2-1 1.5c.6 1.2 1.3 2 2.5 2.5L7 6l2 2-1.5 1.5C4.5 9.5.5 5.5.5 2.5z" fill="#7cc242"/></svg>555 010 2040</span>
    <span><svg width="6" height="5" viewBox="0 0 10 8"><rect x=".5" y=".5" width="9" height="7" fill="none" stroke="#7cc242"/><path d="M.5.5L5 4.5 9.5.5" fill="none" stroke="#7cc242"/></svg>coach@courtsideplan.com</span>
    <span><svg width="6" height="6" viewBox="0 0 10 10"><circle cx="5" cy="5" r="4.3" fill="none" stroke="#7cc242"/><ellipse cx="5" cy="5" rx="2" ry="4.3" fill="none" stroke="#7cc242"/><path d="M.7 5h8.6" stroke="#7cc242"/></svg>courtsideplan.com</span>
  </div>
  <div class="abs foot"></div>
</section>

<!-- Mission & Culture -->
<section class="page mission">
  <svg class="abs" style="left:0;top:0" width="235" height="333"><polygon points="133,0 235,0 235,114 106,114" fill="#7cc242"/></svg>
  <div class="photo" style="left:112px;top:22px;width:123px;height:106px;clip-path:polygon(15px 0,123px 0,109px 106px,0 106px);background:linear-gradient(160deg,#c9c6c0 0,#8c5a36 45%,#e07a1c 55%,#6a3a1e 80%,#2a1a20 100%)" role="img" aria-label="Basketball above a rim and net in front of a blurred arena crowd"></div>
  <h2 class="abs heading head"><span class="n">Mission</span><span class="sq"></span><br><span class="g">Statement</span></h2>
  <p class="abs body">Develop a winning basketball program on and off the court with an unwavering commitment to developing players/coaches with high character, unparalleled work ethic, unassailable integrity, leadership, and life skills.</p>
  <div class="abs team"><h2 class="head"><span class="g">Team<br>Building<br>and</span><br><span class="w">Culture</span></h2></div>
  <ul class="list" style="left:109px;top:202px;width:112px">
    <li>Coachable, Good attitude, Body Language, life/ Practice Habits.</li>
    <li>Respect; Coaches, Teaches, Family, Yourself, Friends, School, and Community</li>
    <li>Look for a mentor and be a mentor.</li>
    <li>Teach them to be part of something greater than themselves.</li>
    <li>Retain high character kids, highly motivated, hard workers, unselfish, communicators.</li>
    <li>Building confidence from practice, repetition, routines, and game experience.</li>
    <li>Teach Failure is one step closer to success.</li>
  </ul>
  <span class="pnum g" style="left:8px;top:314px">- 02 -</span>
</section>

<!-- Practice Philosophy -->
<section class="page practice">
  <svg class="abs" style="left:0;top:0" width="235" height="213"><polygon points="100,0 235,0 235,135" fill="#7cc242"/><polygon points="100,0 113,0 235,122 235,135" fill="#fff" opacity="0"/></svg>
  <div class="abs bar"></div>
  <h2 class="abs heading head"><span class="g">Practice</span><br><span class="n">Philosophy</span></h2>
  <ul class="list" style="left:16px;top:60px;width:104px">
    <li>Practice is harder than games.</li>
    <li>Every minute counts, detailed plans, work on weakness, enhance strengths.</li>
    <li>Fundamental development, High IQ development.</li>
    <li>Teach how to play (not just teach plays), Teach Actions</li>
    <li>Create good habits for life and basketball.</li>
    <li>Create an environment to learn to play successfully in game stress (make good decisions).</li>
  </ul>
  <div class="photo" style="left:131px;top:50px;width:93px;height:92px;background:linear-gradient(180deg,#8fb3d6 0,#c9d6de 45%,#e8c894 70%,#6f6a60 100%)" role="img" aria-label="Two players jumping at an outdoor hoop in bright sunlight"></div>
  <div class="abs" style="left:152px;top:135px;width:16px;height:15px;background:var(--navy)"></div>
  <div class="abs lower"></div>
  <div class="photo" style="left:86px;top:189px;width:63px;height:64px;background:linear-gradient(150deg,#d9e2ea 0,#5b7fa8 45%,#2d3e5a 100%)" role="img" aria-label="Hands typing on a laptop showing skill training screens"></div>
  <h2 class="abs actions-title head"><span class="g">Teach</span> <span class="w">Actions</span></h2>
  <p class="abs actions">DHO, Drag, BD, Ghost, Pin down, Stagger Screen, Curls, Pops, Fades, Flash, Euro Cuts, Stacks, Slips, Shallow cuts, Shuffle cuts, Elevator Screens, GAG, V-cut, RPP, Shape up, Back Screens, Dives.</p>
  <span class="pnum w" style="left:8px;top:314px">- 03 -</span>
</section>

<!-- Offensive / Defensive -->
<section class="page offense">
  <div class="abs top"></div>
  <div class="abs tick" style="left:35px"></div>
  <div class="abs tick" style="left:124px"></div>
  <h2 class="abs col-head head g" style="left:35px">Offensive<span class="light w">Philosophy</span></h2>
  <h2 class="abs col-head head w" style="left:124px">Defensive<span class="light">Philosophy</span></h2>
  <div class="abs box" style="left:30px;width:88px;background:var(--box-grey)">
    <ul class="list">
      <li>Transition, Fast Break, Organized freedom.</li>
      <li>Dribble Drive, Attack, Drive, and kick, Create double gaps.</li>
      <li>Motion offense, constant action, put the defense on its heels.</li>
      <li>Run Actions, DHO, BD, Drag, Ghost Screens, Staggers, Elevator, Shuffle, Slip.</li>
      <li>Quick sets, mismatches, read and react, and counters.</li>
      <li>Great Spacing, timing and ball movement.</li>
      <li>Create open shots and get to the foul line.</li>
    </ul>
  </div>
  <div class="abs box" style="left:121px;width:86px;background:var(--box-green)">
    <ul class="list">
      <li>Speed up your opponent, make them uncomfortable, change looks.</li>
      <li>Great team defense, weak side help, stunt, up the line, ball you man.</li>
      <li>Close out, box out.</li>
      <li>Trap corners, baseline shift, offensive charges, stay connected, help is coming.</li>
      <li>Communication on every movement.</li>
      <li>Full court pressure and take their best players out of the game.</li>
    </ul>
  </div>
  <h2 class="abs system head n">System</h2>
  <ul class="list plain" style="left:26px;top:266px;width:80px">
    <li>Play Chess not Checkers.</li><li>Multi man offense</li><li>Multiple Defenses</li><li>Press and speed up.</li><li>Out Execute your opponent</li><li>Out work your opponent</li>
  </ul>
  <svg class="abs" style="left:0;top:0" width="235" height="333"><polygon points="135,238 219,238 200,320 118,320" fill="#7cc242"/></svg>
  <div class="photo" style="left:118px;top:243px;width:92px;height:69px;clip-path:polygon(11px 0,92px 0,80px 69px,0 69px);background:linear-gradient(135deg,#b9c2c6 0,#5f8d72 40%,#3d4450 75%,#8a8f94 100%)" role="img" aria-label="Coach and players kneeling around a court diagram"></div>
  <span class="pnum n" style="left:8px;top:316px">- 04 -</span>
</section>

<!-- Numbers & Life Skills -->
<section class="page numbers">
  <div class="abs tag" style="top:26px;background:var(--green)">By The<br>Numbers</div>
  <p class="abs val" style="top:33px">Make +2, Miss -2, Fouls -1, Assts +2, Fouls -1, Assts +2, T/O -2, Steals +2, Reb +1, Blk +1, O/C +5, Defl +1.</p>
  <div class="abs line" style="top:75px"></div>
  <div class="abs tag" style="top:77px;background:var(--navy)">Game<br>Goals</div>
  <p class="abs val" style="top:83px">Steals (20), Assists (20), T/O (&lt;10), O/C (3), OP/S (&lt;40), T/S (&gt;60), Rbs (&gt;30), FG% (&gt;40), FT% (&gt;70)</p>
  <div class="abs line" style="top:126px"></div>
  <div class="abs tag" style="top:128px;background:var(--green)">Game<br>Etiquette</div>
  <p class="abs val" style="top:133px">Huddle FT, Warmups, Subs, Stretch, Body Language, Clean up, Pickup TM, Dress Code, Sportsmanship, time-outs.</p>
  <div class="photo lower" role="img" aria-label="Players leaping for a rebound under a hoop, toned green and navy"></div>
  <div class="abs vr" style="top:205px;height:42px"></div>
  <h3 class="abs sub head g" style="top:207px">Life Skills</h3>
  <p class="abs txt" style="top:221px">Disciple, Prepare, mentally tough, Confidence, Resilient, Communication, Teamwork, Goals, Understand the numbers, Be creative, More than one way to win, Adapt, Trust, Be on time, little things matter, you are always being watched.</p>
  <div class="abs vr" style="top:265px;height:52px"></div>
  <h3 class="abs sub head g" style="top:266px">Educations</h3>
  <p class="abs txt" style="top:280px;width:95px">Grades and citizenship first.<br><span style="display:block;height:3px"></span>Monitoring and communication with the teachers, Classroom Behavior.<br><span style="display:block;height:3px"></span>Tutoring and homework.</p>
  <span class="pnum w" style="left:208px;top:316px">- 05 -</span>
</section>

<!-- Mental Health & Success -->
<section class="page wellness">
  <svg class="abs" style="left:0;top:0" width="235" height="333"><polygon points="0,0 90,0 235,0 235,136 0,237" fill="#1f1d5c"/><polygon points="0,0 90,0 0,39" fill="#7cc242"/></svg>
  <div class="circle c1">
    <h3 class="head" style="margin-top:43px;font-size:11.5px"><span class="n">Mental</span> <span class="g">Health</span></h3>
    <p style="font-size:4.7px;line-height:7px;margin:5px auto 0;width:100px">Create a Routine, Stay Active, get proper sleep, ask for help and Listen to your body.</p>
  </div>
  <div class="circle c2">
    <h3 class="head w" style="margin-top:34px;font-size:13.5px">Success</h3>
    <p class="w" style="font-size:4.3px;line-height:7.2px;margin:6px auto 0;width:108px">Success is the peace of mind which is a direct result of the self-satisfaction in knowing you did your best to become the best that you are capable of becoming.</p>
    <p class="w" style="font-size:4.3px;margin-top:3px">- Coach R. Hale -</p>
  </div>
  <div class="circle c3" role="img" aria-label="Gold trophy with scattered stars on a teal background"></div>
  <span class="pnum g" style="left:8px;top:316px">- 06 -</span>
</section>

<!-- Parent & Winner -->
<section class="page parent">
  <div class="abs rail"></div>
  <div class="abs label w" style="top:18px;background:var(--green)">Be a Great Parent</div>
  <ul class="list plain navy-dot" style="left:15px;top:46px;width:115px;font-size:5px;line-height:8.3px">
    <li>Tell them I love to watch you play.</li>
    <li>Learn from losses, move on, No excuses.</li>
    <li>Teach them to be part of something greater than themselves.</li>
    <li>Do not coach your child, Focus on the process.</li>
    <li>Cheer for all.</li>
    <li>Teach them to play for the love of, the game, teammates, and competition.</li>
  </ul>
  <div class="abs" style="left:190px;top:118px;width:23px;height:50px;background:#fff"></div>
  <div class="abs" style="left:71px;top:149px;width:50px;height:52px;background:var(--green)"></div>
  <div class="photo" style="left:98px;top:126px;width:108px;height:107px;background:linear-gradient(160deg,#f3d9a4 0,#7aa35a 35%,#3f6a3a 65%,#8b8f8c 100%)" role="img" aria-label="Player leaping toward an outdoor hoop with trees behind"></div>
  <div class="abs label g" style="top:219px;background:var(--navy)">Be a Winner</div>
  <ul class="list plain" style="left:15px;top:248px;width:125px;font-size:5px;line-height:8.3px">
    <li>A winner makes mistake and says" I was wrong".</li>
    <li>A winner goes through a problem, not around it.</li>
    <li>A winner knows what to fight for and what to compromise on.</li>
    <li>A winner respects his Coaches/Parents/Teachers and tries to learn from them.</li>
    <li>A winner is responsible for more than his job.</li>
  </ul>
  <div class="abs" style="left:0;top:315px;width:18px;height:18px;background:var(--green)"></div>
  <span class="pnum w" style="left:202px;top:316px">- 07 -</span>
</section>

</body>
</html>
```